Poster for pawn shop lobby

Looking for green and gold as my colors, like the picture shown of my old poster. This time I'm contemplating with doing pictures as well as just text. Here are ideas of things I buy and give loans on. We want to emphasize jewelry, laptops, game systems, tools. I'm open-minded.
Old & Broken Gold
Jewelry & Collectibles
Diamonds
Video Games & Systems
Up-to-date Computers & Laptops
Tablets
Cameras
Power Tools
Home & Garden Equipment
Sports Equipment
Watches
Antique Collectibles
Musical Instruments
And anything else of value
Shop

```html
<!DOCTYPE html>
<html lang="en">
<head>
<meta charset="utf-8">
<title>We Buy &amp; Loan – Lobby Poster</title>
<link rel="stylesheet" href="https://fonts.googleapis.com/css2?family=Varela+Round&display=swap">
<style>
  :root {
    --field: #0c3a23;
    --field-deep: #072817;
    --gold-line: #f3d33c;
    --gold-soft: #e6c24a;
    --text: #ffffff;
    --coin-light: rgba(232, 204, 84, 0.34);
    --coin-mid: rgba(190, 160, 50, 0.28);
    --coin-dark: rgba(120, 100, 24, 0.22);
    --gap: 9px;
  }
  * { margin: 0; padding: 0; box-sizing: border-box; }
  html, body { width: 1200px; height: 1200px; overflow: hidden; background: var(--field-deep); }
  .poster {
    position: relative;
    width: 1200px;
    height: 1200px;
    background: var(--field-deep);
    border: 6px solid var(--gold-line);
    font-family: "Varela Round", "Arial Rounded MT Bold", sans-serif;
    color: var(--text);
    overflow: hidden;
  }
  .board {
    position: absolute;
    left: 48px;
    top: 51px;
    width: 1092px;
    height: 1087px;
    background: var(--gold-line);
    display: flex;
    flex-direction: column;
    gap: var(--gap);
    padding: var(--gap) 0;
  }
  .row { flex: 1; display: flex; gap: 20px; }
  .cell {
    background: var(--field);
    display: flex;
    align-items: center;
    justify-content: center;
    gap: 22px;
    text-align: center;
    white-space: nowrap;
    line-height: 1.05;
  }
  .cell--left { border-radius: 0 75px 75px 0; }
  .cell--right { flex: 1; border-radius: 75px 0 0 75px; }
  .row--1 .cell--left { width: 534px; }
  .row--2 .cell--left { width: 768px; }
  .row--3 .cell--left { width: 344px; }
  .row--4 .cell--left { width: 546px; }
  .row--5 .cell--left { width: 230px; }

  .item { position: relative; z-index: 2; display: flex; flex-direction: column; align-items: center; }
  .item--bold { text-shadow: 0 0 1px var(--text), 0 0 1px var(--text); }
  .size-xs  { font-size: 42px; }
  .size-s   { font-size: 48px; }
  .size-m   { font-size: 57px; }
  .size-l   { font-size: 64px; }
  .size-xl  { font-size: 90px; }
  .size-sub { font-size: 30px; line-height: 1.2; color: var(--gold-soft); }
  .stack .size-l, .stack .size-s { margin-bottom: 6px; }

  .photo {
    position: relative;
    z-index: 2;
    flex: none;
    width: 120px;
    height: 120px;
    border-radius: 50%;
    border: 4px solid var(--gold-line);
  }
  .photo--jewelry { background: radial-gradient(circle at 35% 35%, #fff4c2, #d9ae3a 55%, #7a5a12); }
  .photo--laptop  { background: linear-gradient(160deg, #cfd6dc, #6f7a84 60%, #2b3238); }
  .photo--games   { background: linear-gradient(160deg, #5a5f6a, #23262c 70%, #101214); }
  .photo--tools   { background: linear-gradient(160deg, #f2c230, #c88a12 55%, #3a3a3a); }

  .dollar-mark {
    position: absolute;
    z-index: 1;
    left: 300px;
    top: 20px;
    width: 600px;
    height: 1150px;
    border-radius: 46% / 30%;
    background: radial-gradient(ellipse at 40% 35%, var(--coin-light), var(--coin-mid) 55%, var(--coin-dark));
    pointer-events: none;
  }
</style>
</head>
<body>
  <main class="poster">
    <section class="board">
      <div class="row row--1">
        <div class="cell cell--left">
          <div class="photo photo--jewelry" role="img" aria-label="Photo of gold rings and necklaces"></div>
          <span class="item size-s">Jewelry &amp;<br>Collectibles</span>
        </div>
        <div class="cell cell--right">
          <span class="item item--bold size-l">Computers<br>&amp; Laptops</span>
          <div class="photo photo--laptop" role="img" aria-label="Photo of an open laptop"></div>
        </div>
      </div>
      <div class="row row--2">
        <div class="cell cell--left">
          <div class="photo photo--games" role="img" aria-label="Photo of a game console and controller"></div>
          <span class="item size-s">Video Games &amp; Systems</span>
        </div>
        <div class="cell cell--right"><span class="item size-m">Tablets</span></div>
      </div>
      <div class="row row--3">
        <div class="cell cell--left"><span class="item size-l">Watches</span></div>
        <div class="cell cell--right"><span class="item size-m">Old &amp; Broken Gold</span></div>
      </div>
      <div class="row row--4">
        <div class="cell cell--left">
          <div class="photo photo--tools" role="img" aria-label="Photo of a cordless power drill"></div>
          <span class="item size-l">Power Tools</span>
        </div>
        <div class="cell cell--right"><span class="item item--bold size-xl">Diamonds</span></div>
      </div>
      <div class="row row--5">
        <div class="cell cell--left"><span class="item size-xs">Cameras</span></div>
        <div class="cell cell--right">
          <span class="item stack">
            <span class="size-s">Home &amp; Garden Equipment</span>
            <span class="size-sub">Sports Equipment · Musical Instruments</span>
            <span class="size-sub">Antiques &amp; Anything Else of Value</span>
          </span>
        </div>
      </div>
    </section>
    <div class="dollar-mark" role="img" aria-label="Large translucent gold 3D dollar sign behind the listings"></div>
  </main>
</body>
</html>
```